Campaign Flyer for a local election

Black and white election flyer

See information below to be included:

Re-elect Dorian
Experienced Willows Board Member
Experienced NYC Principal
Experienced leader

One Year Board Accomplishments:
-Installed New Park Lights (Bollards)
-Red Brick Road Repair Project
-Established Closer Ties with Our local precinct to frequently monitor the community with directed security patrols. Requested an increased police presence.
-Met with the 62nd Precinct Officials & Assemblywoman, Marla Quintrell to discuss our security issues
- Focused on maintenance of streetlights to make brighter streets
-Negotiated Contract & Hired Our New Landscaper, Oakhollow Landscapers
-Major Homeowner Shrub Replacement Project
- Addressing Standing Water in our Park (Installed French Drain)
- Replaced and upgraded all 5 outdoor circuit breaker panels
-Write monthly community newsletters
-Sewer cleaning project (had all community catch basins cleaned)
-Carefully overseeing our new school project. Coordinating with the sponsor and the school directors
-Delivered a very healthy budget to the community
-Works closely with our committees
-Events: Zoo event, Petting Zoo, Outdoor Movie Night, Egg Hunt

It is my intent to seek re-election.
(Photo) Dorian Lindqvist
-Dedicated to improving our community
-Hard-working…He gets thing done!
-Trustworthy

. .

Please note, I am submitting new information under accomplishments. The list of accomplishments should be in the same sequence, starting with: Met with the 62nd Precinct....
Please carefully review.
----------------------------------------------------------------------------------------------------------------------------------------------------------------

Re-elect Dorian
Experienced NYC Principal
Experienced leader

Last Year’s Board Accomplishments:

-Met with the 62nd Precinct Officials & Assemblywoman, Marla Quintrell, to discuss our security issues. Requested increased police presence.
-Established a strong partnership with the 62nd precinct to frequently monitor the community with directed security patrols.
-Replaced all new park lights (Bollards) to make the park brighter
- Focused on maintenance of streetlights to make streets brighter
-‘Fixing Our Streets Project’ (Repaired all cracked/missing red bricks)
-Homeowner Shrub Replacement Project (Replaced hundreds of bushes)
- I write the monthly community newsletter
-Carefully overseeing our new school project. Coordinating with the sponsor and the school director
-Monitoring C of O’s and homeowners Insurance

(Photo) Dorian Lindqvist
-Hard-working! I get things done!
-Trustworthy

. .

Re-elect Dorian
Experienced NYC Principal
Experienced leader

(Photo) Dorian Lindqvist
-Trustworthy

. .

Target Market(s)

A Community electing a Board Member

Industry/Entity Type

residential election

Requirements
Must have
• all black, white and grey print. Flyers will not be printed in color
Nice to have
• See the information in the attachment below containing all my accomplishments
Should not have
• color

```html
<!DOCTYPE html>
<html lang="en">
<head>
<meta charset="utf-8">
<title>Re-elect Dorian — Campaign Flyer</title>
<link rel="stylesheet" href="https://fonts.googleapis.com/css2?family=Archivo+Black&family=Russo+One&family=Fredoka:wght@600;700&family=Rubik:ital,wght@1,400&display=swap">
<style>
  :root {
    --ink: #0b0b0b;
    --paper: #ffffff;
    --stage: #e4e4e4;
    --photo-light: #b9b9b9;
    --photo-dark: #4a4a4a;
  }
  * { box-sizing: border-box; margin: 0; padding: 0; }
  html, body { width: 1200px; height: 1200px; overflow: hidden; background: var(--stage); }

  .flyer {
    position: absolute; left: 190px; top: 30px;
    width: 820px; height: 1140px;
    background: var(--ink);
    box-shadow: 0 6px 18px rgba(0,0,0,.25);
    overflow: hidden;
  }
  .flyer-shapes { position: absolute; inset: 0; }

  .title {
    position: absolute; left: 0; right: 0; top: 36px;
    text-align: center;
    font-family: "Archivo Black", sans-serif;
    font-size: 84px; line-height: 1; letter-spacing: -1px;
    color: var(--ink);
    -webkit-text-stroke: 14px var(--paper);
    paint-order: stroke fill;
    text-shadow: 0 0 10px rgba(255,255,255,.8);
  }

  .credentials { position: absolute; left: 60px; top: 150px; display: flex; align-items: center; }
  .credentials-main {
    font-family: "Russo One", sans-serif; font-size: 42px; color: var(--paper);
    letter-spacing: 1px; padding-right: 26px;
  }
  .credentials-divider { width: 3px; height: 100px; background: var(--paper); }
  .credentials-list {
    list-style: none; padding-left: 26px;
    font-family: "Russo One", sans-serif; font-size: 22px; line-height: 1.2;
    color: var(--paper); letter-spacing: 1px;
  }

  .accomplishments-heading {
    position: absolute; left: 50px; top: 296px;
    font-family: "Russo One", sans-serif; font-size: 31px;
    letter-spacing: 3px; color: var(--ink);
  }

  .accomplishments {
    position: absolute; left: 44px; top: 350px; width: 480px;
    list-style: none;
    font-family: "Rubik", sans-serif; font-style: italic; font-weight: 400;
    font-size: 14.5px; line-height: 1.18; color: var(--ink);
  }
  .accomplishments li { position: relative; padding-left: 34px; margin-bottom: 3px; }
  .accomplishments li::before {
    content: ""; position: absolute; left: 2px; top: 4px;
    width: 12px; height: 8px; background: var(--ink);
  }

  .intent {
    position: absolute; left: 0; right: 0; top: 792px; text-align: center;
    font-family: "Fredoka", sans-serif; font-weight: 700; font-size: 38px;
    line-height: 1.1; letter-spacing: 2px; color: var(--ink);
  }

  .portrait-frame {
    position: absolute; left: 50px; top: 890px; width: 230px; height: 210px;
    background: var(--paper); padding: 14px;
  }
  .portrait {
    width: 100%; height: 100%;
    background: linear-gradient(160deg, var(--photo-light), var(--photo-dark));
  }

  .candidate { position: absolute; left: 320px; top: 905px; color: var(--paper); }
  .candidate-name {
    font-family: "Fredoka", sans-serif; font-weight: 700; font-size: 58px;
    letter-spacing: 2px; line-height: 1;
  }
  .candidate-traits {
    list-style: none; margin-top: 22px; margin-left: 16px;
    font-family: "Russo One", sans-serif; font-size: 22px; line-height: 1.3; letter-spacing: 1px;
  }
</style>
</head>
<body>
<main class="flyer">
  <svg class="flyer-shapes" viewBox="0 0 820 1140" width="820" height="1140" aria-hidden="true">
    <polygon fill="var(--paper)" points="0,255 350,262 405,292 455,262 820,248 820,860 0,860"/>
    <polygon fill="var(--ink)" points="820,300 720,330 640,366 585,378 568,470 548,520 562,570 522,622 537,722 600,748 820,738"/>
    <polygon fill="var(--ink)" points="0,850 260,878 560,870 640,852 820,858 820,1140 0,1140"/>
  </svg>
  <svg class="flyer-shapes" viewBox="0 0 820 1140" width="820" height="1140" role="img" aria-label="Photo of dune grass beside the sea">
    <defs>
      <linearGradient id="shoreTone" x1="0" y1="0" x2="0" y2="1">
        <stop offset="0" stop-color="#d6d6d6"/>
        <stop offset="0.3" stop-color="#8f8f8f"/>
        <stop offset="1" stop-color="#555555"/>
      </linearGradient>
    </defs>
    <polygon fill="url(#shoreTone)" points="800,362 700,380 664,400 604,410 594,480 578,530 594,576 564,626 574,708 640,728 800,720"/>
  </svg>

  <h1 class="title">Re-elect Dorian</h1>

  <div class="credentials">
    <span class="credentials-main">EXPERIENCED</span>
    <span class="credentials-divider"></span>
    <ul class="credentials-list">
      <li>Willows Board Member</li>
      <li>NYC Principal</li>
      <li>Leader</li>
    </ul>
  </div>

  <h2 class="accomplishments-heading">ONE YEAR BOARD ACCOMPLISHMENTS</h2>

  <ul class="accomplishments">
    <li>Installed New Park Lights (Bollards)</li>
    <li>Red Brick Road Repair Project</li>
    <li>Established Closer Ties with Our local precinct to frequently monitor the community with directed security patrols. Requested an increased police presence.</li>
    <li>Met with the 62nd Precinct Officials &amp; Assembly woman, Marla Quintrell to discuss our security issues</li>
    <li>Focused on maintenance of streetlights to make brighter streets</li>
    <li>Negotiated Contract &amp; Hired Our New Landscaper, Oakhollow Landscapers</li>
    <li>Major Homeowner Shrub Replacement Project</li>
    <li>Addressing Standing Water in our Park (Installed French Drain)</li>
    <li>Replaced and upgraded all 5 outdoor circuit breaker panels</li>
    <li>Write monthly community newsletters</li>
    <li>Sewer cleaning project (had all community catch basins cleaned)</li>
    <li>Carefully overseeing our new school project. Coordinating with the sponsor and the school directors</li>
    <li>Delivered a very healthy budget to the community</li>
    <li>Works closely with our committees</li>
    <li>Events: Zoo event, Petting Zoo, Outdoor Movie Night, Egg Hunt</li>
  </ul>

  <p class="intent">It is my intent to seek re-election</p>

  <div class="portrait-frame">
    <div class="portrait" role="img" aria-label="Portrait photo of Dorian Lindqvist"></div>
  </div>

  <div class="candidate">
    <p class="candidate-name">Dorian Lindqvist</p>
    <ul class="candidate-traits">
      <li>Dedicated to improving our community</li>
      <li>Hard-working...He gets thing done!</li>
      <li>Trustworthy</li>
    </ul>
  </div>
</main>
</body>
</html>
```